Redesign our iOS App Design mockups

- Redesign our current Veltro App Mockup
- Keep the design simple so that programmers do not have to do too much extra work to make your design work.
- Look at the attached website screenshot for the overall look and feel, and color scheme
- Convert the attached vector logo to iOS Icon format.
- Deliver all graphics in the density required for Veltro QL Prime.
- I have attached the current iOS mockup in a .ZIP file but you can view it here as well: https://boards.mockvault.net/share/QWTRPL8HNB2

Target Market(s)

Mostly Male Internet Consumers between the ages of 20 and 35

Industry/Entity Type

Internet

Colors

Designer to choose colors to be used in the design.

Requirements
Must have
• - Deliver all graphics in the density required for Veltro QL Prime
• - Should also look good on Tabrix and Tabrix pro
• - Design type should be “FLAT.”
• - Spell out fonts used in the design and where they are used. Also, include font sizes.
• - Please use ALL the elements in each page and use all placements and text EXACTLY. Please do not improvise with text or components.
• I have designed the mockup exactly the way I like it. I just want it to made to look better.
Should not have

```html
<!DOCTYPE html>
<html lang="en">
<head>
<meta charset="UTF-8">
<title>HAVENLINK – Log In</title>
<link href="https://fonts.googleapis.com/css2?family=Roboto:wght@400;500;700&display=swap" rel="stylesheet">
<style>
  :root {
    --coral: #f0604f;
    --coral-border: #e8604f;
    --blush: #fbd3cd;
    --ink: #2b2b2b;
    --label: #333333;
    --muted: #5a5a5a;
    --placeholder: #9a9a9a;
    --field-border: #bdbdbd;
    --white: #ffffff;
  }
  * { box-sizing: border-box; margin: 0; padding: 0; }
  html, body {
    width: 1200px;
    height: 2598px;
    overflow: hidden;
    background: var(--white);
    font-family: 'Roboto', Arial, sans-serif;
  }
  .screen { position: relative; width: 1200px; height: 2598px; overflow: hidden; }
  .header-wave { position: absolute; left: 0; top: 0; width: 1200px; height: 900px; }
  .login-card {
    position: absolute;
    left: 102px; top: 544px;
    width: 995px; height: 1517px;
    background: var(--white);
    border: 10px solid var(--coral-border);
    border-top: none;
  }
  .brand { position: absolute; left: 0; top: 675px; width: 1200px; text-align: center; }
  .brand-mark {
    width: 170px; height: 170px;
    margin: 0 auto;
    border-radius: 50%;
    background: var(--coral);
  }
  .brand-name {
    margin-top: 120px;
    font-size: 54px;
    font-weight: 700;
    letter-spacing: 1px;
    color: var(--ink);
    line-height: 1;
  }
  .field-label {
    position: absolute;
    left: 173px;
    font-size: 51px;
    font-weight: 500;
    color: var(--label);
    line-height: 1;
  }
  .label-username { top: 1158px; }
  .label-password { top: 1462px; }
  .text-field {
    position: absolute;
    left: 173px;
    width: 854px; height: 112px;
    border: 3px solid var(--field-border);
    border-radius: 56px;
    display: flex; align-items: center;
    padding: 0 54px;
    font-size: 38px;
    color: var(--placeholder);
  }
  .field-username { top: 1232px; }
  .field-password { top: 1539px; justify-content: space-between; }
  .eye-icon { width: 52px; height: 52px; margin-right: -16px; }
  .btn {
    position: absolute;
    display: flex; align-items: center; justify-content: center;
    background: var(--coral);
    color: var(--white);
    font-weight: 700;
  }
  .btn-login {
    left: 368px; top: 1782px;
    width: 467px; height: 128px;
    border-radius: 64px;
    font-size: 58px;
  }
  .signup-prompt {
    position: absolute;
    left: 115px; top: 2280px;
    font-size: 45px;
    color: var(--muted);
    line-height: 1;
  }
  .btn-signup {
    left: 723px; top: 2259px;
    width: 355px; height: 96px;
    border-radius: 48px;
    font-size: 51px;
  }
</style>
</head>
<body>
<main class="screen">
  <svg class="header-wave" viewBox="0 0 1200 900" aria-hidden="true">
    <path d="M0 0 H1200 V850 C900 960 300 960 0 812 Z" fill="var(--blush)"/>
    <path d="M0 0 H1200 V838 C880 900 320 900 0 752 Z" fill="var(--coral)"/>
  </svg>

  <section class="login-card" aria-label="Log in form"></section>

  <div class="brand">
    <div class="brand-mark"></div>
    <div class="brand-name">HAVENLINK</div>
  </div>

  <label class="field-label label-username">User Name</label>
  <div class="text-field field-username">Enter your Email</div>

  <label class="field-label label-password">Password</label>
  <div class="text-field field-password">
    <span>Enter Your Password</span>
    <svg class="eye-icon" viewBox="0 0 24 24" aria-hidden="true">
      <path fill="#7a7a7a" d="M12 5C7 5 2.7 8.1 1 12c1.7 3.9 6 7 11 7s9.3-3.1 11-7c-1.7-3.9-6-7-11-7zm0 11.5A4.5 4.5 0 1 1 12 7.5a4.5 4.5 0 0 1 0 9zm0-7a2.5 2.5 0 1 0 0 5 2.5 2.5 0 0 0 0-5z"/>
    </svg>
  </div>

  <div class="btn btn-login">Log In</div>

  <p class="signup-prompt">Don't have an Account yet?</p>
  <div class="btn btn-signup">Sign Up</div>
</main>
</body>
</html>
```